BUsiness Card

We need a unique business card design for a new aesthetic practice, Meadowlark Skin & Vitality, P.A. The reverse of the card should be an appointment card.

```html
<!DOCTYPE html>
<html lang="en">
<head>
<meta charset="utf-8">
<title>Meadowlark Skin &amp; Vitality – Business &amp; Appointment Card</title>
<link rel="stylesheet" href="https://fonts.googleapis.com/css2?family=Open+Sans:wght@400;600&display=swap">
<style>
  :root {
    --navy: #0b4a68;
    --teal: #1ba39c;
    --ink: #1d1d1f;
    --paper: #ffffff;
    --box: #cfcfcf;
    --stage: #ebe7df;
  }
  * { box-sizing: border-box; margin: 0; padding: 0; }
  html, body { width: 1200px; height: 942px; overflow: hidden; }
  body {
    background: var(--stage);
    font-family: "Open Sans", Arial, sans-serif;
    color: var(--ink);
    position: relative;
  }
  .card {
    position: absolute;
    width: 560px;
    height: 320px;
    background: var(--paper);
    overflow: hidden;
    box-shadow: 0 6px 18px rgba(0,0,0,.15);
  }
  .card--front { left: 50px; top: 520px; }
  .card--back { left: 590px; top: 90px; }

  /* front */
  .front__band {
    position: absolute; left: 0; right: 0; bottom: 0; height: 78px;
    background: var(--navy);
    display: flex; align-items: center; padding-left: 34px;
  }
  .website { color: #fff; font-size: 19px; letter-spacing: 3px; }
  .identity { position: absolute; left: 34px; top: 30px; }
  .identity__name { font-size: 26px; font-weight: 600; line-height: 1.1; }
  .identity__title { font-size: 15px; color: var(--navy); margin-top: 2px; }
  .identity__rule { width: 44px; height: 2px; background: var(--navy); margin-top: 12px; }
  .contacts { position: absolute; left: 34px; top: 124px; list-style: none; }
  .contacts li { display: flex; align-items: center; gap: 10px; font-size: 15px; margin-bottom: 6px; }
  .contacts svg { width: 16px; height: 16px; fill: var(--navy); flex: none; }
  .brand { position: absolute; display: flex; align-items: center; gap: 10px; }
  .brand__dot { border-radius: 50%; background: var(--navy); flex: none; }
  .brand__name { color: var(--navy); font-weight: 600; line-height: 1.15; }
  .card--front .brand { right: 30px; top: 120px; }
  .card--front .brand__dot { width: 46px; height: 46px; }
  .card--front .brand__name { font-size: 19px; }

  /* back */
  .card--back .brand { left: 30px; top: 26px; }
  .card--back .brand__name { font-size: 18px; }
  .back__panel {
    position: absolute; right: 0; top: 0; bottom: 0; width: 170px;
    background: var(--navy);
  }
  .appt { position: absolute; left: 30px; top: 96px; width: 340px; }
  .appt__heading { color: var(--teal); font-size: 19px; margin-bottom: 20px; }
  .appt__who { display: flex; align-items: flex-end; gap: 8px; font-size: 14px; }
  .appt__line { flex: 1; border-bottom: 1.5px solid var(--navy); height: 18px; }
  .days { display: flex; gap: 18px; list-style: none; margin-top: 18px; font-size: 14px; }
  .days li { display: flex; align-items: center; gap: 5px; }
  .days li::after { content: ""; width: 11px; height: 11px; background: var(--box); }
  .when { display: flex; gap: 20px; margin-top: 20px; font-size: 14px; color: var(--teal); }
  .when span { display: flex; align-items: flex-end; gap: 6px; flex: 1; }
  .when span::after { content: ""; flex: 1; border-bottom: 1.5px solid var(--teal); height: 16px; }
</style>
</head>
<body>

<section class="card card--front" aria-label="Business card front">
  <div class="identity">
    <p class="identity__name">Your Name</p>
    <p class="identity__title">Job Title</p>
    <div class="identity__rule"></div>
  </div>
  <ul class="contacts">
    <li><svg viewBox="0 0 16 16"><path d="M3 1h3l1.5 3.5-2 1.3a9 9 0 0 0 4.7 4.7l1.3-2L15 10v3a2 2 0 0 1-2 2A12 12 0 0 1 1 3a2 2 0 0 1 2-2z"/></svg>000 000 0000</li>
    <li><svg viewBox="0 0 16 16"><path d="M1 3h14v10H1z M1 3l7 6 7-6" fill="none" stroke="#0b4a68" stroke-width="1.6"/></svg>youremail@xyz.com</li>
    <li><svg viewBox="0 0 16 16"><path d="M8 0a5.5 5.5 0 0 0-5.5 5.5C2.5 10 8 16 8 16s5.5-6 5.5-10.5A5.5 5.5 0 0 0 8 0zm0 8a2.5 2.5 0 1 1 0-5 2.5 2.5 0 0 1 0 5z"/></svg>your adress</li>
  </ul>
  <div class="brand">
    <span class="brand__dot"></span>
    <p class="brand__name">Meadowlark<br>Skin &amp; Vitality</p>
  </div>
  <div class="front__band"><p class="website">www.yourwebsite.com</p></div>
</section>

<section class="card card--back" aria-label="Appointment card">
  <div class="brand">
    <p class="brand__name">Meadowlark Skin &amp; Vitality</p>
  </div>
  <div class="appt">
    <p class="appt__heading">Appointment</p>
    <p class="appt__who"><span class="appt__line"></span>has an appointment</p>
    <ul class="days">
      <li>Mon</li><li>Tue</li><li>Wed</li><li>Thu</li><li>Fri</li>
    </ul>
    <p class="when"><span>Date:</span><span>Time:</span></p>
  </div>
  <div class="back__panel"></div>
</section>

</body>
</html>
```